Product Label with Company Logo & Product Information

I am looking for a new label design for one of my products, Candied Pecans. I am including an old label that I made, but it does not "pop" on the current packaging. See image of current packaging attached as well.

I want the design to ultimately be something that I can take and order a roll of labels/stickers. Please stick within standard label/sticker sizes (round or square). Please include final size as well.

Must Haves:
(1) Company logo (any color variation-see attached logo images).
(2) All wording on the old label
(3) Label size can not be more than 2 in. x 4 in. (I would actually like them a little smaller). They seem kind of big as they are right now.

```html
<!DOCTYPE html>
<html lang="en">
<head>
<meta charset="utf-8">
<title>Meadow Hive – Gourmet Candied Pecans Label</title>
<link href="https://fonts.googleapis.com/css2?family=Chewy&family=Signika:wght@400;500;600&family=Source+Sans+3:wght@400&display=swap" rel="stylesheet">
<style>
  :root{
    --stage:#3d3d3d;
    --label-yellow:#f1ec2e;
    --panel-white:#ffffff;
    --ink:#58585a;
    --note:#ffffff;
  }
  *{box-sizing:border-box;margin:0;padding:0}
  html,body{width:1200px;height:1200px;overflow:hidden;background:var(--stage)}
  .stage{position:relative;width:1200px;height:1200px}
  .label{
    position:absolute;left:118px;top:325px;width:964px;height:511px;
    background:var(--label-yellow);overflow:hidden;
    box-shadow:0 6px 18px rgba(0,0,0,.35);
  }
  .label__art{position:absolute;inset:0;width:964px;height:511px}
  .label__content{position:absolute;inset:0;text-align:center;color:var(--ink)}
  .brand{
    position:absolute;left:0;right:0;top:100px;
    display:flex;justify-content:center;align-items:center;gap:12px;
    font-family:"Signika",sans-serif;font-weight:600;font-size:38px;line-height:1;color:var(--ink);
  }
  .brand__dot{width:30px;height:30px;border-radius:50%;background:var(--label-yellow)}
  .product-kicker{
    position:absolute;left:0;right:0;top:228px;
    font-family:"Signika",sans-serif;font-weight:500;font-size:35px;line-height:1;
  }
  .product-name{position:absolute;inset:0;margin:0;font-size:inherit;font-weight:normal}
  .product-name__art{position:absolute;inset:0;width:964px;height:511px}
  .product-name__text{
    font-family:"Chewy",cursive;font-size:60px;fill:var(--ink);
  }
  .details{
    position:absolute;left:0;right:0;top:366px;
    font-family:"Signika",sans-serif;font-weight:500;font-size:20px;line-height:31.5px;
  }
  .spec-note{
    position:absolute;left:0;right:0;top:918px;text-align:center;
    font-family:"Source Sans 3",sans-serif;font-size:44px;line-height:62px;color:var(--note);
  }
</style>
</head>
<body>
<main class="stage">
  <section class="label">
    <svg class="label__art" viewBox="0 0 964 511" xmlns="http://www.w3.org/2000/svg">
      <defs>
        <radialGradient id="burst" cx="50%" cy="50%" r="65%">
          <stop offset="0" stop-color="#f7f38a"/>
          <stop offset="0.6" stop-color="#f4f06a"/>
          <stop offset="1" stop-color="#f1ec2e"/>
        </radialGradient>
      </defs>
      <rect class="sunburst" width="964" height="511" fill="url(#burst)" role="img" aria-label="Sunburst of white rays radiating on yellow"/>
      <path class="info-panel"
        d="M278,76 Q292,49 322,49 L641,49 Q671,49 685,76 L768,230 Q782,256 768,282 L685,435 Q671,462 641,462 L322,462 Q292,462 278,435 L198,282 Q184,256 198,230 Z"
        fill="var(--panel-white)" stroke="var(--ink)" stroke-width="3"/>
      <line class="divider" x1="222" y1="219" x2="742" y2="219" stroke="var(--ink)" stroke-width="2" stroke-dasharray="1.5 6" stroke-linecap="round"/>
      <line class="divider" x1="248" y1="346" x2="720" y2="346" stroke="var(--ink)" stroke-width="2" stroke-dasharray="1.5 6" stroke-linecap="round"/>
    </svg>
    <div class="label__content">
      <div class="brand"><span class="brand__dot"></span><span>Meadow Hive</span></div>
      <p class="product-kicker">Gourmet</p>
      <h1 class="product-name">
        <svg class="product-name__art" viewBox="0 0 964 511" xmlns="http://www.w3.org/2000/svg">
          <text class="product-name__text" x="482" y="326" text-anchor="middle" textLength="490" lengthAdjust="spacingAndGlyphs">CANDIED PECANS</text>
        </svg>
      </h1>
      <p class="details">Made with Cinnamon, Brown Sugar &amp; Salt<br>Order more @ (555)014-2870<br>Meadow Hive Market, LLC</p>
    </div>
  </section>
  <p class="spec-note">Final size: 2 by 4 inches<br>bleed: .125 inches</p>
</main>
</body>
</html>
```